Corbelle Group - Business Cards

We would need to design our Company Business Cards for the following People:

1. Martin Cole
Director/Licensee-In-Charge
M: 0417 524 903
T: (02) 7354 2260
E: martin@corbelle.com.au
Website: www.corbellegroup.com

2. Derek Holm
Project Manager
M: 0428 613 954
T: (02) 7354 2260
E: derek@corbellegroup.com

3. Priya Venkataraman
Property Officer
M: 0439 271 806
T: (02) 7354 2260
E: priya@corbellegroup.com

Address: Level 9, 42 Harlow Road W, Parramatta NSW 2150
The above address is the SAME for ALL Cards.

This Card is to be Double-Sided.
Front - With the above Information & Details.
Back - Showing the Services:
Property Services, Financial Solutions, Special Projects.

ALL Office Locations:
Sydney: (02) 7354 2260
Melbourne: (03) 9412 5063
Brisbane: (07) 3275 4190
Malaysia (JB): (+601) 8340 2967
Singapore: (+65) 9481 2736

We intend on making a Design/Template for the Business Card & duplicating these Business Cards for the above 3x People.
Please USE & REFER to the above FULL Name, Job Title, Mobile, Office Phone, Email & Website.

```html
<!DOCTYPE html>
<html lang="en">
<head>
<meta charset="utf-8">
<title>Corbelle Group – Business Cards</title>
<link rel="stylesheet" href="https://fonts.googleapis.com/css2?family=Mulish:ital,wght@0,400;0,600;0,700;1,400&display=swap">
<style>
  :root {
    --stage: #8f8c89;
    --card: #1b1b1b;
    --ink: #f2f2f2;
    --accent: #d6d21c;
  }
  * { margin: 0; padding: 0; box-sizing: border-box; }
  html, body { width: 1200px; height: 1200px; overflow: hidden; }
  body {
    background: var(--stage);
    font-family: "Mulish", sans-serif;
    color: var(--ink);
    display: flex;
    flex-direction: column;
    align-items: center;
    justify-content: center;
    gap: 80px;
  }
  .card {
    position: relative;
    width: 820px;
    height: 500px;
    background: var(--card);
    box-shadow: 0 10px 24px rgba(0,0,0,.35);
  }
  .wordmark { text-align: center; font-weight: 400; color: var(--ink); }
  .wordmark .name { display: block; font-size: 44px; letter-spacing: 18px; padding-left: 18px; line-height: 1; }
  .wordmark .sub { display: block; font-size: 22px; letter-spacing: 9px; padding-left: 9px; margin-top: 10px; }
  .accent { color: var(--accent); }

  /* back */
  .card--back .wordmark { position: absolute; top: 92px; left: 0; right: 0; }
  .services { position: absolute; top: 230px; left: 0; right: 0; text-align: center; font-size: 17px; line-height: 1.45; }
  .services .label { color: var(--accent); font-weight: 700; }
  .offices { position: absolute; top: 340px; left: 0; right: 0; text-align: center; font-size: 17px; line-height: 1.55; }
  .offices .label { color: var(--accent); font-style: italic; }
  .offices .city { color: var(--accent); }
  .offices .row span + span { margin-left: 22px; }

  /* front */
  .card--front .brand { position: absolute; left: 60px; top: 170px; width: 400px; }
  .brand .rule { width: 44px; height: 2px; background: var(--accent); margin: 16px auto 12px 290px; }
  .brand address { font-style: normal; text-align: center; font-size: 17px; line-height: 1.4; }
  .divider { position: absolute; left: 490px; top: 130px; width: 2px; height: 190px; background: var(--accent); }
  .person { position: absolute; left: 522px; top: 140px; }
  .person h1 { font-size: 30px; font-weight: 600; color: var(--accent); line-height: 1.1; }
  .person .role { font-size: 16px; margin: 4px 0 8px; }
  .contact { list-style: none; font-size: 16px; line-height: 1.6; }
  .contact li { display: flex; align-items: center; gap: 10px; }
  .contact svg { width: 13px; height: 13px; flex: none; fill: var(--accent); }
</style>
</head>
<body>

<section class="card card--back" aria-label="Card back">
  <div class="wordmark">
    <span class="name">CORBELLE</span>
    <span class="sub">Group</span>
  </div>
  <div class="services">
    <div class="label">We provide :</div>
    <div>Special Projects.</div>
    <div>Financial Solutions.</div>
    <div>Property Services.</div>
  </div>
  <div class="offices">
    <div class="label">ALL Office Locations:</div>
    <div class="row"><span><span class="city">Sydney:</span> (02) 7354 2260</span><span><span class="city">Melbourne:</span> (03) 9412 5063</span><span><span class="city">Brisbane:</span> (07) 3275 4190</span></div>
    <div class="row"><span><span class="city">Malaysia (JB):</span> (+601) 8340 2967</span><span><span class="city">Singapore:</span> (+65) 9481 2736</span></div>
  </div>
</section>

<section class="card card--front" aria-label="Card front">
  <div class="brand">
    <div class="wordmark">
      <span class="name">CORBELLE</span>
      <span class="sub">Group</span>
    </div>
    <div class="rule"></div>
    <address>Level 9, 42 Harlow Road W<br>Parramatta NSW 2150</address>
  </div>
  <div class="divider"></div>
  <div class="person">
    <h1>Martin Cole</h1>
    <div class="role">Director/Licensee-In-Charge</div>
    <ul class="contact">
      <li><svg viewBox="0 0 16 16"><path d="M4 1l3 3-2 2c1 2 3 4 5 5l2-2 3 3-2 3C7 15 1 9 1 3z"/></svg>+ 0417 524 903</li>
      <li><svg viewBox="0 0 16 16"><path d="M1 6c0-3 14-3 14 0v2h-4V6H5v2H1zM3 9h10l1 6H2z"/></svg>+(02) 7354 2260</li>
      <li><svg viewBox="0 0 16 16"><path d="M1 3h14v10H1zM2 4l6 5 6-5z" fill-rule="evenodd"/></svg>martin@corbelle.com.au</li>
      <li><svg viewBox="0 0 16 16"><circle cx="8" cy="8" r="7"/></svg>www.corbellegroup.com</li>
    </ul>
  </div>
</section>

</body>
</html>
```